『千里堀水路めぐりウォーク』
2019年10月27日(日)
集合場所:楓野丘公園第5駐車場
受付:8:30~
スタート:9:00
参加費:1500円(会員)1800円(一般)
所要時間:約4時間
定員:20名(先着順)
受付締切:3日前まで

『スラックラインとマウンテンバイクを体験しよう』
2019年11月2日(土) 2019年11月16日(土)
集合場所:ウィンドテラスもりさとアクティブパーク
受付:13:00~
参加費:2500円(一般)2000円(会員)
所要時間:約2時間
定員:10名(先着順)
受付締切:3日前まで
主催:青凪クラブ/「第17回公益信託はればれ基金」
A4
片面
緑系
• 高解像度JPG (.jpg)
• PNG形式 (.png)
PDF形式での納品もお願い致します。

採用の理由は以下の2点になります。

・明るさと分かりやすさのバランスが良かった点
・目を引くレイアウト及びデザインであった点

以上となります。

この度は急なご依頼にも関わらず
ご提案下さり誠にありがとう御座います。

写真や情報の提供など至らない点が多くあったと思いますが
素晴らしい提案をして頂き大変助かりました。

また機会が御座いましたら
宜しくお願い致します。

```html
<!DOCTYPE html>
<html lang="ja">
<head>
<meta charset="utf-8">
<title>運動の秋イベント</title>
<link rel="stylesheet" href="https://fonts.googleapis.com/css2?family=Zen+Maru+Gothic:wght@500;700;900&family=M+PLUS+Rounded+1c:wght@800&display=swap">
<style>
:root{
  --cream:#fbf3d6;
  --stripe:#f6e9bd;
  --green:#3f9b2f;
  --green-dark:#2d7a22;
  --orange:#f08a1c;
  --orange-light:#f7b04a;
  --pink:#e0407a;
  --white:#ffffff;
  --ink:#333333;
  --highlight:#fff35c;
}
*{box-sizing:border-box;margin:0;padding:0}
html,body{width:849px;height:1200px;overflow:hidden}
body{font-family:"Zen Maru Gothic",sans-serif;color:var(--ink);background:var(--white)}
.poster{position:relative;width:849px;height:1200px;overflow:hidden;
  background:repeating-linear-gradient(135deg,var(--cream) 0 14px,var(--stripe) 14px 28px);
  border:10px solid var(--orange-light)}
.title{position:absolute;font-family:"M PLUS Rounded 1c",sans-serif;font-weight:800;color:var(--green)}
.walk-title{left:22px;top:18px;font-size:48px;line-height:1.12;letter-spacing:2px}
.walk-title span{background:linear-gradient(transparent 55%,var(--highlight) 55%)}
.walk-date{position:absolute;left:440px;top:14px;font-size:58px;line-height:1.2;color:var(--orange);font-family:"M PLUS Rounded 1c",sans-serif;font-weight:800;white-space:nowrap}
.walk-date small{font-size:34px}
.photo{position:absolute;border:4px solid var(--white);box-shadow:0 2px 4px rgba(0,0,0,.2)}
.p-bridge{left:22px;top:140px;width:400px;height:215px;background:linear-gradient(180deg,#b9d4ea 0 45%,#7fae5c 45% 100%)}
.p-canal1{left:22px;top:365px;width:195px;height:200px;background:linear-gradient(160deg,#8bb56a,#4f7d3a)}
.p-canal2{left:227px;top:365px;width:195px;height:200px;background:linear-gradient(200deg,#a5c07e,#5a7d45)}
.tag{position:absolute;left:210px;top:150px;background:var(--white);color:var(--green-dark);font-weight:700;font-size:15px;padding:2px 10px;border-radius:4px}
.info{position:absolute;left:440px;top:98px;width:370px;display:grid;grid-template-columns:1fr 1fr;gap:6px}
.cell{background:var(--white);text-align:center;border:2px solid var(--orange)}
.cell.full{grid-column:span 2}
.cell h3{background:var(--orange);color:var(--white);font-size:16px;font-weight:700;padding:2px 0}
.cell p{font-size:17px;font-weight:700;padding:4px 2px;line-height:1.3}
.season{position:absolute;left:440px;top:450px;width:370px;height:110px;background:var(--white);border:4px solid var(--pink);border-radius:14px;text-align:center;padding-top:8px}
.season .s1{color:var(--pink);font-size:30px;font-weight:900;font-family:"M PLUS Rounded 1c",sans-serif}
.season .s2{color:var(--pink);font-size:44px;font-weight:900;font-family:"M PLUS Rounded 1c",sans-serif;line-height:1}
.host{position:absolute;left:440px;top:570px;width:370px;font-size:12px;font-weight:700;text-align:center}
.slack-title{left:22px;top:605px;font-size:44px;line-height:1.2;letter-spacing:1px}
.slack-dates{position:absolute;left:22px;top:722px;font-family:"M PLUS Rounded 1c",sans-serif;font-weight:800;color:var(--orange);font-size:54px;line-height:1.2;letter-spacing:1px;white-space:nowrap}
.slack-dates small{font-size:30px}
.slack-dates .gap{display:inline-block;width:40px}
.table2{position:absolute;left:22px;top:805px;width:789px;display:grid;grid-template-columns:100px 1fr 100px 1fr 100px 1fr;grid-auto-rows:32px;gap:5px}
.table2 .lbl,.table2 .val{display:flex;align-items:center;justify-content:center;font-size:17px;font-weight:700;border:2px solid var(--orange)}
.table2 .lbl{background:var(--orange);color:var(--white);font-size:16px}
.table2 .val{background:var(--white)}
.table2 .span5{grid-column:span 5}
.table2 .span3{grid-column:span 3}
.p-mtb{left:22px;top:928px;width:380px;height:225px;background:linear-gradient(180deg,#cfe1ef 0 35%,#78a94f 35% 100%)}
.p-line{left:430px;top:928px;width:380px;height:225px;background:linear-gradient(180deg,#b7d2ea 0 50%,#86b25a 50% 100%)}
.bubble{position:absolute;width:100px;height:100px;border-radius:50%;background:var(--white);border:3px solid var(--green);color:var(--green-dark);font-size:14px;font-weight:700;display:flex;align-items:center;justify-content:center;text-align:center;line-height:1.3}
.b-left{left:34px;top:1040px}
.b-right{left:700px;top:1045px}
</style>
</head>
<body>
<main class="poster">
  <h1 class="title walk-title"><span>千里堀水路</span><br><span>めぐりウォーク</span></h1>
  <div class="walk-date">10月27日<small>(日)</small></div>

  <div class="photo p-bridge" role="img" aria-label="水路にかかる橋と山並みの風景写真"></div>
  <div class="tag">楓野丘から10km</div>
  <div class="photo p-canal1" role="img" aria-label="草に囲まれた水路の写真"></div>
  <div class="photo p-canal2" role="img" aria-label="水路沿いの小道の写真"></div>

  <section class="info">
    <div class="cell full"><h3>集合場所</h3><p>楓野丘公園第5駐車場</p></div>
    <div class="cell"><h3>受付</h3><p>受付　8:30～<br>スタート 9:00～</p></div>
    <div class="cell"><h3>所要時間</h3><p>約4時間</p></div>
    <div class="cell"><h3>参加費</h3><p>1500円(会員)<br>1800円(一般)</p></div>
    <div class="cell"><h3>定員</h3><p>20名(先着順)</p></div>
    <div class="cell full"><h3>受付締切</h3><p>3日前まで</p></div>
  </section>

  <div class="season"><div class="s1">運動の</div><div class="s2">秋イベント</div></div>
  <p class="host">主催：青凪クラブ／「第17回公益信託はればれ基金」</p>

  <h2 class="title slack-title">スラックラインと<br>マウンテンバイクを体験しよう</h2>
  <div class="slack-dates">11月2日<small>(土)</small><span class="gap"></span>11月16日<small>(土)</small></div>

  <section class="table2">
    <div class="lbl">集合場所</div>
    <div class="val span5">ウィンドテラスもりさとアクティブパーク</div>
    <div class="lbl">受付</div>
    <div class="val">13:00～</div>
    <div class="lbl">参加費</div>
    <div class="val span3">2500円(一般)　2000円(会員)</div>
    <div class="lbl">所要時間</div>
    <div class="val">約2時間</div>
    <div class="lbl">定員</div>
    <div class="val">10名(先着順)</div>
    <div class="lbl">受付締切</div>
    <div class="val">3日前まで</div>
  </section>

  <div class="photo p-mtb" role="img" aria-label="芝生の広場でマウンテンバイクに乗る参加者の写真"></div>
  <div class="photo p-line" role="img" aria-label="スラックラインを体験する参加者の写真"></div>
  <div class="bubble b-left">マウンテン<br>バイクで<br>森林浴</div>
  <div class="bubble b-right">講師付きで<br>初心者も<br>安心</div>
</main>
</body>
</html>
```